Vel-Trax.ch is looking for business card letterhead and envelope C5 with WOW effect

We need a strong business card for our company Vel-Trax.ch, logo is available. You want a black or dark background on which the logo Stark r% 26 # 252; appears. Letterhead and envelope in C5 format should be in a similar design, but does not have to be We need a strong business card for our company Vel-Trax.ch, logo is available. A black or dark background is desired, on which the logo Stark comes across. The letterhead and the envelope in C5 format should have a similar design.

Target Market(s)

Private customers as well as entrepreneurs

Contact Information for Business Card

E-mail: info@vel-trax.ch
Web.www.Vel-Trax.ch
Tel: +41 ( 0 ) 79 684 3027
Adresse:
Lindenhaldeweg 14
9403 Brenzikon

Hier kann man Icons verwenden für Email,Tel und Adressse

Font styles to use
Other font styles liked:
• Dubai,bold

Colors

Designer to choose colors to be used in the design.

Requirements
Must have
• WOW effect
Nice to have
• R% 26 # 252; back business card with our service listings. - VEHICLE LABELING - SHOP WINDOW LABELING - STICKERS AND MUCH MORE ... in red color

```html
<!DOCTYPE html>
<html lang="en">
<head>
<meta charset="utf-8">
<title>Vel-Trax.ch – Stationery</title>
<link href="https://fonts.googleapis.com/css2?family=Open+Sans:wght@400;700&family=Roboto:wght@400;500&display=swap" rel="stylesheet">
<style>
  :root{
    --bg:#2a2a2a;
    --ink:#111111;
    --card:#0b0b0b;
    --paper:#f7f7f5;
    --yellow:#f5c518;
    --yellow-soft:#f7e7b0;
    --text-grey:#4a4a4a;
    --white:#ffffff;
  }
  *{box-sizing:border-box;margin:0;padding:0}
  html,body{width:1200px;height:800px;overflow:hidden;background:var(--bg)}
  body{position:relative;font-family:"Open Sans",sans-serif}
  address{font-style:normal}

  .brand-name{font-family:"Open Sans",sans-serif;font-weight:700;letter-spacing:1px;text-transform:uppercase;display:flex;align-items:center;gap:8px;white-space:nowrap}
  .brand-dot{width:10px;height:10px;border-radius:50%;background:var(--yellow);flex:none}

  .icon{width:10px;height:10px;flex:none}
  .contact-line{display:flex;align-items:center;gap:6px;white-space:nowrap}

  /* Letterhead */
  .letterhead{position:absolute;left:40px;top:40px;width:510px;height:720px;background:var(--paper);color:var(--text-grey);overflow:hidden}
  .letterhead-pattern{position:absolute;right:0;bottom:0;width:260px;height:330px;background:radial-gradient(ellipse at 70% 60%,var(--yellow-soft),rgba(247,231,176,0) 70%);z-index:0}
  .letterhead .brand-name{position:absolute;left:50px;top:76px;font-size:20px;color:var(--ink);z-index:1}
  .letterhead-contact{position:absolute;right:50px;top:48px;font-size:10.5px;line-height:1.55;color:var(--text-grey);z-index:1}
  .letterhead-body{position:absolute;left:50px;top:170px;width:410px;font-size:10px;line-height:1.55;z-index:1}
  .letterhead-body p{margin-bottom:12px}

  /* Business cards */
  .card{position:absolute;width:300px;height:172px;background:var(--card);border-bottom:2px solid var(--yellow);color:var(--white);overflow:hidden}
  .card-front{left:590px;top:60px}
  .card-front .brand-name{position:absolute;left:20px;top:38px;font-size:15px;color:var(--white)}
  .card-person{position:absolute;left:20px;top:70px}
  .card-person-name{font-family:"Roboto",sans-serif;font-weight:500;font-size:10px;color:var(--yellow);letter-spacing:.5px;text-transform:uppercase}
  .card-person-role{font-family:"Roboto",sans-serif;font-size:8px;color:var(--white)}
  .card-contact{position:absolute;left:20px;top:104px;font-family:"Roboto",sans-serif;font-size:7.5px;line-height:1.5;color:var(--white)}
  .card-pattern{position:absolute;right:0;top:0;width:120px;height:150px;background:linear-gradient(225deg,var(--yellow) 0%,rgba(245,197,24,.6) 50%,rgba(245,197,24,0) 100%)}

  .card-back{left:590px;top:270px}
  .card-back .brand-name{position:absolute;left:110px;top:56px;font-size:16px;color:var(--white)}
  .card-back-pattern{position:absolute;left:18px;top:30px;width:80px;height:80px;background:radial-gradient(circle,var(--yellow) 0%,rgba(245,197,24,.5) 55%,rgba(245,197,24,0) 75%)}
  .service-list{position:absolute;left:16px;right:16px;bottom:16px;display:flex;gap:8px;font-family:"Roboto",sans-serif;font-size:6.5px;color:var(--white);text-transform:uppercase;list-style:none;white-space:nowrap}
  .service-list li::before{content:"";display:inline-block;width:4px;height:4px;border-radius:50%;background:var(--yellow);margin-right:4px;vertical-align:middle}

  /* Envelope C5 */
  .envelope{position:absolute;left:920px;top:60px;width:250px;height:354px;background:var(--card);border-bottom:2px solid var(--yellow);border-left:2px solid var(--yellow);overflow:hidden}
  .envelope .brand-name{position:absolute;left:40px;top:50px;font-size:20px;color:var(--white)}
  .envelope-pattern{position:absolute;right:0;bottom:0;width:230px;height:230px;background:radial-gradient(ellipse at 70% 60%,var(--yellow) 0%,rgba(245,197,24,.55) 45%,rgba(245,197,24,0) 75%)}
</style>
</head>
<body>

<svg width="0" height="0" style="position:absolute" aria-hidden="true">
  <defs>
    <symbol id="icon-phone" viewBox="0 0 10 10"><circle cx="5" cy="5" r="5" fill="#f5c518"/><path d="M3 2.6l1 .1.4 1.2-.6.5a4 4 0 0 0 1.8 1.8l.5-.6 1.2.4.1 1c-2.5.3-4.7-1.9-4.4-4.4z" fill="#111"/></symbol>
    <symbol id="icon-mail" viewBox="0 0 10 10"><circle cx="5" cy="5" r="5" fill="#f5c518"/><rect x="2.4" y="3.2" width="5.2" height="3.6" fill="none" stroke="#111" stroke-width=".7"/><path d="M2.4 3.2L5 5.3l2.6-2.1" fill="none" stroke="#111" stroke-width=".7"/></symbol>
    <symbol id="icon-web" viewBox="0 0 10 10"><circle cx="5" cy="5" r="5" fill="#f5c518"/><circle cx="5" cy="5" r="2.6" fill="none" stroke="#111" stroke-width=".6"/><path d="M2.4 5h5.2M5 2.4c-1.2 1.4-1.2 3.8 0 5.2M5 2.4c1.2 1.4 1.2 3.8 0 5.2" fill="none" stroke="#111" stroke-width=".5"/></symbol>
    <symbol id="icon-pin" viewBox="0 0 10 10"><circle cx="5" cy="5" r="5" fill="#f5c518"/><path d="M5 8s-2.2-2.3-2.2-3.8a2.2 2.2 0 0 1 4.4 0C7.2 5.7 5 8 5 8z" fill="#111"/><circle cx="5" cy="4.2" r=".8" fill="#f5c518"/></symbol>
  </defs>
</svg>

<section class="letterhead">
  <div class="letterhead-pattern" role="img" aria-label="Faint yellow honeycomb pattern"></div>
  <address class="letterhead-contact">
    <div>Lindenhaldeweg 14</div>
    <div>9408 Brenzikon</div>
    <div class="contact-line"><svg class="icon"><use href="#icon-phone"/></svg>+41 ( 0 ) 79 684 3027</div>
    <div class="contact-line"><svg class="icon"><use href="#icon-mail"/></svg>info@vel-trax.ch</div>
    <div class="contact-line"><svg class="icon"><use href="#icon-web"/></svg>www.Vel-Trax.ch</div>
  </address>
  <div class="brand-name"><span class="brand-dot"></span>Vel-Trax.ch</div>
  <div class="letterhead-body">
    <p>Dear customer,</p>
    <p>Lorem ipsum dolor sit amet, consectetur adipisicing elit, sed do eiusmod tempor incididunt ut labore et dolore magna aliqua. Ut enim ad minim veniam, quis nostrud exercitation ullamco laboris nisi ut aliquip ex ea commodo consequat. Duis aute irure dolor in reprehenderit in voluptate velit esse cillum dolore eu fugiat nulla pariatur. Excepteur sint occaecat cupidatat non proident, sunt in culpa qui officia deserunt mollit anim id est laborum.</p>
    <p>Lorem ipsum dolor sit amet, consectetur adipisicing elit, sed do eiusmod tempor incididunt ut labore et dolore magna aliqua. Ut enim ad minim veniam, quis nostrud exercitation ullamco laboris nisi ut aliquip ex ea commodo consequat. Duis aute irure dolor in reprehenderit in voluptate velit esse cillum dolore eu fugiat nulla pariatur. Excepteur sint occaecat cupidatat non proident, sunt in culpa qui officia deserunt mollit anim id est laborum.</p>
    <p>Lorem ipsum dolor sit amet, consectetur adipisicing elit, sed do eiusmod tempor incididunt ut labore et dolore magna aliqua. Ut enim ad minim veniam, quis nostrud exercitation ullamco laboris nisi ut aliquip ex ea commodo consequat. Duis aute irure dolor in reprehenderit in voluptate velit esse cillum dolore eu fugiat nulla pariatur. Excepteur sint occaecat cupidatat non proident, sunt in culpa qui officia deserunt mollit anim id est laborum.</p>
    <p>Lorem ipsum dolor sit amet, consectetur adipisicing elit, sed do eiusmod tempor incididunt ut labore et dolore magna aliqua. Ut enim ad minim veniam, quis nostrud exercitation ullamco laboris nisi ut aliquip ex ea commodo consequat. Duis aute irure dolor in reprehenderit.</p>
    <p>Lorem ipsum dolor sit amet, consectetur adipisicing elit, sed do eiusmod tempor incididunt ut labore et dolore magna aliqua. Ut enim ad minim veniam, quis nostrud exercitation ullamco laboris nisi ut aliquip ex ea commodo consequat.</p>
    <p>Yours Sincerely,</p>
  </div>
</section>

<section class="card card-front">
  <div class="card-pattern" role="img" aria-label="Yellow honeycomb pattern"></div>
  <div class="brand-name">Vel-Trax.ch</div>
  <div class="card-person">
    <div class="card-person-name">Marco Liechti</div>
    <div class="card-person-role">Director</div>
  </div>
  <address class="card-contact">
    <div class="contact-line"><svg class="icon"><use href="#icon-phone"/></svg>+41 ( 0 ) 79 684 3027</div>
    <div class="contact-line"><svg class="icon"><use href="#icon-mail"/></svg>info@vel-trax.ch</div>
    <div class="contact-line"><svg class="icon"><use href="#icon-web"/></svg>www.Vel-Trax.ch</div>
    <div class="contact-line"><svg class="icon"><use href="#icon-pin"/></svg>Lindenhaldeweg 14 9408 Brenzikon</div>
  </address>
</section>

<section class="card card-back">
  <div class="card-back-pattern" role="img" aria-label="Small yellow honeycomb cluster"></div>
  <div class="brand-name">Vel-Trax.ch</div>
  <ul class="service-list">
    <li>Vehicle labeling</li>
    <li>Shop window labeling</li>
    <li>Stickers and much more</li>
  </ul>
</section>

<section class="envelope">
  <div class="envelope-pattern" role="img" aria-label="Large yellow honeycomb pattern"></div>
  <div class="brand-name">Vel-Trax.ch</div>
</section>

</body>
</html>
```